sign business needs card design

I need a very clean design for my business card.
It is a sign company. Banners By Noon is the name of the business.
Our colors are orange, yellow. But I want a very professional card.
But you can use any colors. I like a black background with orange letters or a white back with a clean look. No cartoon or kiddy looking print. The info. I need on the card is as follows.
Banners By Noon
318.555.0172 ph.
318.555.0199 fax.
email.bannersbynoon@mailvista.net
web.bannersbynooninc.com
4187 N. Maplecrest Lane Ste. 2b
Dale Hutchins

```html
<!DOCTYPE html>
<html lang="en">
<head>
<meta charset="utf-8">
<title>Banners By Noon – Business Card</title>
<link rel="stylesheet" href="https://fonts.googleapis.com/css2?family=Encode+Sans+Condensed:wght@400;500&family=Open+Sans:wght@400;600&display=swap">
<style>
  :root {
    --canvas: #e9e6dc;
    --card: #ffffff;
    --band: #474747;
    --band-dark: #3a3a3a;
    --orange: #ef4a14;
    --ghost: #f7e0d8;
    --yellow: #ffd400;
    --amber: #f7941d;
    --red: #e8202a;
    --icon: #8a8f99;
  }
  * { margin: 0; padding: 0; box-sizing: border-box; }
  html, body { width: 1200px; height: 960px; overflow: hidden; }
  body {
    background: var(--canvas);
    position: relative;
    font-family: "Encode Sans Condensed", "Arial Narrow", sans-serif;
  }
  .card {
    position: absolute;
    left: 250px;
    width: 700px;
    height: 400px;
    background: var(--card);
    overflow: hidden;
    box-shadow: 0 4px 14px rgba(0,0,0,0.18);
  }
  .card--front { top: 60px; }
  .card--back { top: 500px; }

  /* front */
  .front__name {
    position: absolute; left: 42px; top: 118px;
    color: var(--orange); font-size: 48px; font-weight: 400;
    letter-spacing: -0.5px;
  }
  .front__ghost {
    position: absolute; left: 44px; top: 172px;
    color: var(--ghost); font-size: 52px; letter-spacing: 26px;
  }
  .contact {
    position: absolute; left: 402px; top: 62px;
    list-style: none;
    font-family: "Open Sans", Arial, sans-serif;
    color: var(--orange); font-size: 14px; line-height: 1.25;
  }
  .contact__item { display: flex; align-items: flex-start; margin-bottom: 8px; }
  .contact__icon { width: 16px; height: 16px; margin-right: 12px; margin-top: 1px; flex-shrink: 0; }
  .stripe {
    position: absolute; left: 0; top: 230px; width: 700px; height: 8px;
    background: linear-gradient(90deg, var(--yellow), var(--amber) 45%, var(--red));
  }
  .band {
    position: absolute; left: 0; top: 238px; width: 700px; height: 162px;
    background: var(--band);
  }
  .band__name {
    position: absolute; left: 0; right: 0; top: 38px; text-align: center;
    color: var(--orange); font-size: 72px; font-weight: 500; letter-spacing: -1px;
  }

  /* back */
  .back__name {
    position: absolute; left: 0; right: 0; top: 62px; text-align: center;
    color: var(--orange); font-size: 88px; font-weight: 400; letter-spacing: -1px;
    line-height: 1;
  }
  .back__reflection {
    position: absolute; left: 0; right: 0; top: 152px; text-align: center;
    color: var(--orange); font-size: 88px; font-weight: 400; letter-spacing: -1px;
    line-height: 1; transform: scaleY(-1); opacity: 0.12;
  }
  .back__wave { position: absolute; left: 0; top: 0; width: 700px; height: 400px; }
  .back__tagline {
    position: absolute; left: 0; right: 0; top: 340px; text-align: center;
    color: var(--orange); font-size: 30px; font-weight: 500;
  }
</style>
</head>
<body>

<section class="card card--front" aria-label="Card front">
  <div class="front__name">Banners By Noon</div>
  <div class="front__ghost" aria-hidden="true">Banners</div>

  <ul class="contact">
    <li class="contact__item">
      <svg class="contact__icon" viewBox="0 0 16 16"><path d="M8 1a4.5 4.5 0 0 0-4.5 4.5C3.5 9 8 15 8 15s4.5-6 4.5-9.5A4.5 4.5 0 0 0 8 1z" fill="var(--icon)"/><circle cx="8" cy="5.5" r="1.7" fill="#fff"/></svg>
      <span>4187 N. Maplecrest Lane Ste. 2b<br>Dale Hutchins</span>
    </li>
    <li class="contact__item">
      <svg class="contact__icon" viewBox="0 0 16 16"><rect x="1" y="6" width="14" height="8" rx="1.5" fill="var(--icon)"/><rect x="4" y="2" width="8" height="5" fill="#b9bec6"/><rect x="4" y="9" width="8" height="2" fill="#fff"/></svg>
      <span>318.555.0199 fax.</span>
    </li>
    <li class="contact__item">
      <svg class="contact__icon" viewBox="0 0 16 16"><path d="M2 6c0-2 2.5-3 6-3s6 1 6 3l-3 1-1-2H6L5 7z" fill="var(--icon)"/><rect x="3" y="8" width="10" height="6" rx="1.5" fill="var(--icon)"/><circle cx="8" cy="11" r="1.6" fill="#fff"/></svg>
      <span>318.555.0172 ph.</span>
    </li>
    <li class="contact__item">
      <svg class="contact__icon" viewBox="0 0 16 16"><circle cx="8" cy="8" r="7" fill="var(--icon)"/><circle cx="8" cy="8" r="2.5" fill="none" stroke="#fff" stroke-width="1.4"/><path d="M10.5 6v3a1.5 1.5 0 0 0 3 0V8" fill="none" stroke="#fff" stroke-width="1.2"/></svg>
      <span>email.bannersbynoon@mailvista.net</span>
    </li>
    <li class="contact__item">
      <svg class="contact__icon" viewBox="0 0 16 16"><circle cx="8" cy="8" r="7" fill="none" stroke="var(--icon)" stroke-width="1.3"/><ellipse cx="8" cy="8" rx="3" ry="7" fill="none" stroke="var(--icon)" stroke-width="1"/><path d="M1 8h14M2.5 4.5h11M2.5 11.5h11" stroke="var(--icon)" stroke-width="1"/></svg>
      <span>web.bannersbynooninc.com</span>
    </li>
  </ul>

  <div class="stripe"></div>
  <div class="band">
    <div class="band__name">Banners By Noon</div>
  </div>
</section>

<section class="card card--back" aria-label="Card back">
  <div class="back__name">Banners By Noon</div>
  <div class="back__reflection" aria-hidden="true">Banners By Noon</div>
  <svg class="back__wave" viewBox="0 0 700 400" aria-hidden="true">
    <path d="M0 305 C 220 320, 480 300, 700 190 L700 400 L0 400 Z" fill="var(--band-dark)"/>
  </svg>
  <div class="back__tagline">we feel glad to service you</div>
</section>

</body>
</html>
```